Olmo Restaurant & Bar Menu

Want to make current menu more trendy in design. I have attached a pdf of the menu and of the logo. Rather, than being 6 pages I would like to make the menu into "4 pages". The menu will be printed in color.

I am open to designs that will allow the menu to be printed on 11x17 paper that will be folded in half. The "Breakfast" section needs to be its own page and all the way on the back.

As for the cover I am open to just keeping it as a cover with the info I have on it but completely different design/picture change. The logo needs to stay. The cover can also be used as having menu items on there if pulled of correctly.

The readability has to be clear to the guests.

The restaurant is a Mediterranean style and for the area it is priced mid-high. The atmosphere is casual fine dining with Martini & Wine Bar. All are ingredients are fresh never frozen and everything is prepared from scratch.

Industry/Entity Type

Restaurant

Requirements
Must have
• Breakfast on its own page on the back.
Nice to have
• Trendy Design

```html
<!DOCTYPE html>
<html lang="en">
<head>
<meta charset="utf-8">
<title>Olmo Restaurant &amp; Bar – Menu Spread</title>
<link href="https://fonts.googleapis.com/css2?family=Oswald:wght@400;500;600&family=Kalam:wght@400;700&display=swap" rel="stylesheet">
<style>
  :root{
    --backdrop:#d9d9d9;
    --ink:#141b23;
    --blue:#2aa9e0;
    --white:#ffffff;
    --muted:#c9d2da;
    --rule:#8fa0ae;
  }
  *{box-sizing:border-box;margin:0;padding:0}
  html,body{width:1200px;height:781px;overflow:hidden;background:var(--backdrop)}
  .spread{position:absolute;left:40px;top:28px;width:1120px;height:725px;display:flex;box-shadow:0 6px 18px rgba(0,0,0,.25)}
  .page{position:relative;width:560px;height:725px;background:var(--ink);overflow:hidden;color:var(--white)}
  .page + .page{border-left:1px solid #0b1016}
  .page-edge{position:absolute;left:0;right:0;bottom:0;height:10px;background:var(--blue)}

  /* ---------- Breakfast page ---------- */
  .section-banner{position:absolute;left:22px;top:34px;width:500px;height:34px;background:var(--blue);border-radius:0 17px 17px 0;
    font:600 19px/34px "Oswald",sans-serif;text-transform:uppercase;letter-spacing:.5px;padding-left:18px;color:var(--white)}
  .column{position:absolute;width:245px}
  .col-left{left:24px;top:84px}
  .col-right{left:290px;top:84px}
  .col-right .item{margin-bottom:6px}
  .light{left:24px;top:572px;width:512px;display:flex;gap:22px}
  .light .column{position:static}
  .heading{font:600 17px/1.1 "Oswald",sans-serif;color:var(--blue);text-transform:uppercase;letter-spacing:.3px;margin:6px 0 6px}
  .heading-note{font:400 9px/1.2 "Kalam",cursive;color:var(--muted);margin:-4px 0 6px}
  .item{margin-bottom:7px}
  .item-line{display:flex;align-items:flex-end;font:500 11.5px/1.25 "Oswald",sans-serif;color:var(--white)}
  .item-line .leader{flex:1;border-bottom:1px solid var(--rule);margin:0 5px 3px}
  .item-line .price{white-space:nowrap}
  .sub{padding-left:8px}
  .desc{font:400 8.5px/1.2 "Kalam",cursive;color:var(--muted);margin-top:1px}
  .fruit-photo{position:absolute;left:404px;top:526px;width:128px;height:56px;background:#fff;padding:4px;border-radius:3px}
  .fruit-photo .fill{width:100%;height:100%;background:linear-gradient(135deg,#f3c27a,#e2553f 55%,#7bb048)}

  /* ---------- Cover page ---------- */
  .top-rule{position:absolute;left:38px;top:22px;width:330px;height:8px;background:var(--blue)}
  .brand{position:absolute;left:40px;top:52px;display:flex;align-items:center;gap:12px}
  .brand-dot{width:34px;height:34px;border-radius:50%;background:var(--blue)}
  .brand-name{font:600 30px/1 "Oswald",sans-serif;text-transform:uppercase;color:var(--white);letter-spacing:.5px;white-space:nowrap}
  .photo{position:absolute;border:3px solid var(--white)}
  .photo-wraps{left:300px;top:112px;width:240px;height:120px;background:linear-gradient(135deg,#d9b24a,#8a4d2c 55%,#e8d9b8)}
  .photo-pita{left:40px;top:160px;width:250px;height:110px;background:linear-gradient(135deg,#e9e4da,#b7875a 55%,#7aa64a)}
  .photo-waffles{left:110px;top:278px;width:320px;height:154px;background:linear-gradient(135deg,#f1e2bf,#c78a45 50%,#8a4a22)}
  .photo-olives{left:438px;top:240px;width:102px;height:90px;background:linear-gradient(135deg,#5a4a3a,#2a2e22 60%,#d7c9a8)}
  .photo-salad{left:438px;top:336px;width:102px;height:96px;background:linear-gradient(135deg,#7a1a22,#f1ece4 55%,#6f9a3e)}
  .info-band{position:absolute;left:0;right:0;top:444px;height:120px;background:var(--blue);display:flex;justify-content:space-between;padding:16px 28px}
  .contact{font:500 13px/1.5 "Oswald",sans-serif;color:var(--ink);font-style:normal}
  .contact .phone{font-size:15px}
  .contact .web{font-size:17px;font-weight:600;margin-top:4px}
  .services{list-style:none;text-align:right;font:500 12.5px/1.9 "Oswald",sans-serif;color:var(--white);text-transform:uppercase;letter-spacing:.4px}
</style>
</head>
<body>
<main class="spread">

  <!-- Back page: Breakfast -->
  <section class="page page-breakfast">
    <h1 class="section-banner">Breakfast (Served Saturday &amp; Sunday)</h1>

    <div class="column col-left">
      <h2 class="heading">Skillets</h2>
      <div class="item"><div class="item-line"><span>Veggie</span><span class="leader"></span><span class="price">$6.95</span></div>
        <p class="desc">Skillet full of hash browns, onions, peppers, tomatoes &amp; mushrooms topped with cheese and 2 eggs. Served w/ toast.</p></div>
      <div class="item"><div class="item-line"><span>Irish</span><span class="leader"></span><span class="price">$7.95</span></div>
        <p class="desc">Skillet full of hash browns, onions, peppers &amp; corned beef topped with cheese and 2 eggs. Served w/ toast.</p></div>
      <div class="item"><div class="item-line"><span>Melting Pot</span><span class="leader"></span><span class="price">$8.95</span></div>
        <p class="desc">Skillet full of hash browns, ham, bacon, sausage, mushrooms, onions, tomatoes and peppers topped with cheese and 2 eggs. Served with toast.</p></div>
      <div class="item"><div class="item-line"><span>Biscuits &amp; Gravy</span><span class="leader"></span><span class="price">$7.95</span></div>
        <p class="desc">Skillet full of hash browns, onions, peppers &amp; cheese topped w/ homemade biscuit, sausage gravy &amp; 2 eggs.</p></div>

      <h2 class="heading">Omelettes</h2>
      <p class="heading-note">Fluffy Three Egg Omelettes, Served w/ Hash Browns &amp; Toast</p>
      <div class="item"><div class="item-line"><span>Athenian</span><span class="leader"></span><span class="price">$8.95</span></div>
        <p class="desc">Gyro off-the-cone, tomatoes, onions, olives, &amp; feta cheese. Served with side of homemade cucumber sauce.</p></div>
      <div class="item"><div class="item-line"><span>Denver</span><span class="leader"></span><span class="price">$7.95</span></div>
        <p class="desc">Ham, onion, pepper &amp; cheese</p></div>
      <div class="item"><div class="item-line"><span>Veggie</span><span class="leader"></span><span class="price">$8.95</span></div>
        <p class="desc">Onions, peppers, tomatoes &amp; mushrooms</p></div>
      <div class="item"><div class="item-line"><span>Deluxe</span><span class="leader"></span><span class="price">$8.95</span></div>
        <p class="desc">Ham, bacon, sausage, mushrooms, onions, tomatoes and peppers</p></div>
      <div class="item"><div class="item-line"><span>Spinach Pesto</span><span class="leader"></span><span class="price">$8.95</span></div>
        <p class="desc">Sundried tomatoes, spinach, mushrooms &amp; cheese. Topped w/ Pesto Cream Sauce</p></div>
      <div class="item"><div class="item-line"><span>Ham &amp; Cheese</span><span class="leader"></span><span class="price">$6.95</span></div></div>
    </div>

    <div class="column col-right">
      <h2 class="heading">Pancakes, French Toast &amp; Waffles</h2>
      <div class="item"><div class="item-line"><span>Apple Danish French Toast</span><span class="leader"></span><span class="price">$6.95</span></div></div>
      <div class="item"><div class="item-line"><span>Bananas Foster Pancakes</span><span class="leader"></span><span class="price">$7.95</span></div></div>
      <div class="item"><div class="item-line"><span>Strawberry Cake Waffle</span><span class="leader"></span><span class="price">$7.95</span></div></div>
      <div class="item"><div class="item-line"><span>Pancakes or French Toast</span><span class="leader"></span><span class="price">&nbsp;</span></div>
        <div class="item-line sub"><span>2 pcs.</span><span class="leader"></span><span class="price">$4.55 / 3 pcs. $4.95</span></div></div>
      <div class="item"><div class="item-line"><span>Belgium Waffle</span><span class="leader"></span><span class="price">$4.95</span></div></div>

      <h2 class="heading">Eggs &amp; Specialties</h2>
      <div class="item"><div class="item-line"><span>Two Eggs, Hash Browns &amp; Toast</span><span class="leader"></span><span class="price">$4.95</span></div>
        <div class="item-line sub"><span>» With Bacon, Sausage or Ham</span><span class="leader"></span><span class="price">$5.95</span></div>
        <div class="item-line sub"><span>» With Corned Beef Hash</span><span class="leader"></span><span class="price">$6.55</span></div>
        <div class="item-line sub"><span>» With Gyro off-the-cone</span><span class="leader"></span><span class="price">$6.95</span></div></div>
      <div class="item"><div class="item-line"><span>Steak &amp; Eggs</span><span class="leader"></span><span class="price">$13.95</span></div>
        <p class="desc">8oz Prime Cut Steak, 2 Eggs, hash browns, &amp; Toast</p></div>
      <div class="item"><div class="item-line"><span>Chop Steak &amp; Eggs</span><span class="leader"></span><span class="price">$9.95</span></div>
        <p class="desc">10oz Chopped Sirloin Steak, 2 Eggs, hash browns &amp; toast</p></div>
      <div class="item"><div class="item-line"><span>Granny's Breakfast</span><span class="leader"></span><span class="price">$6.95</span></div>
        <p class="desc">Two Eggs scrambled w/ potatoes, ham, onions &amp; peppers topped w/ cheese. Served with toast.</p></div>
      <div class="item"><div class="item-line"><span>3 Deuces</span><span class="leader"></span><span class="price">$6.95</span></div>
        <p class="desc">Two Eggs, Two Pancakes &amp; Two Sausage Links or Bacon Strips</p></div>
      <div class="item"><div class="item-line"><span>Homemade Biscuits &amp; Gravy</span><span class="leader"></span><span class="price">&nbsp;</span></div>
        <div class="item-line sub"><span>Half $3.95 / Full</span><span class="leader"></span><span class="price">$5.95</span></div></div>
    </div>

    <div class="fruit-photo"><div class="fill" role="img" aria-label="Plate of fresh sliced fruit"></div></div>

    <div class="column light">
      <div class="column">
        <h2 class="heading">Light Breakfast</h2>
        <div class="item"><div class="item-line"><span>Egg, Sausage &amp; Cheese Sandwich</span><span class="leader"></span><span class="price">$4.25</span></div></div>
        <div class="item"><div class="item-line"><span>Oatmeal or Cereal</span><span class="leader"></span><span class="price">$3.55</span></div>
          <div class="item-line sub"><span>w/ raisins</span><span class="leader"></span><span class="price">$3.95</span></div></div>
        <div class="item"><div class="item-line"><span>Bagel w/ cream cheese</span><span class="leader"></span><span class="price">$2.55</span></div></div>
      </div>
      <div class="column">
        <h2 class="heading">&nbsp;</h2>
        <div class="item"><div class="item-line"><span>English Muffin or Raisin Toast</span><span class="leader"></span><span class="price">$1.55</span></div></div>
        <div class="item"><div class="item-line"><span>Mediterranean Pita</span><span class="leader"></span><span class="price">$6.95</span></div>
          <p class="desc">Pesto Spread on Pita Bread w/ spinach, tomatoes, feta &amp; an Egg</p></div>
        <div class="item"><div class="item-line"><span>Fresh Fruit Bowl</span><span class="leader"></span><span class="price">$4.95</span></div></div>
      </div>
    </div>

    <div class="page-edge"></div>
  </section>

  <!-- Front cover -->
  <section class="page page-cover">
    <div class="top-rule"></div>
    <div class="brand">
      <span class="brand-dot"></span>
      <span class="brand-name">Olmo Restaurant &amp; Bar</span>
    </div>

    <div class="photo photo-wraps" role="img" aria-label="Grilled gyro wraps with sauce on a platter"></div>
    <div class="photo photo-pita" role="img" aria-label="Pita wrap with fresh vegetables"></div>
    <div class="photo photo-waffles" role="img" aria-label="Belgian waffles topped with glazed chicken"></div>
    <div class="photo photo-olives" role="img" aria-label="Small dish of marinated olives"></div>
    <div class="photo photo-salad" role="img" aria-label="Greek salad with feta on a white plate"></div>

    <div class="info-band">
      <address class="contact">
        <div>48 Harbor Lane - Millbrook, WI 53990</div>
        <div class="phone">555-014-2290</div>
        <div class="web">www.olmorestaurant.com</div>
      </address>
      <ul class="services">
        <li>Serving Breakfast Saturday &amp; Sunday</li>
        <li>Catering &amp; Private Party Hosting Available</li>
        <li>Friday Fish Fry - Saturday Prime Rib</li>
      </ul>
    </div>

    <div class="page-edge"></div>
  </section>

</main>
</body>
</html>
```